Criação de Folder para Alimentos & Bebidas
A empresa queria:
" importamos produtos com nossas marcas e distribuimos para supermercdos e distribuidores "

```html
<!DOCTYPE html>
<html lang="pt-BR">
<head>
<meta charset="utf-8">
<title>Prime Harvest – Folder</title>
<link href="https://fonts.googleapis.com/css2?family=Open+Sans:ital,wght@0,400;0,600;0,700;0,800;1,400&display=swap" rel="stylesheet">
<style>
  :root{
    --ink:#0d0d0d;
    --ink-soft:#1c1c1c;
    --paper:#ffffff;
    --red:#c8151b;
    --red-deep:#8e0c10;
    --yellow:#f4b41a;
    --gold:#e9c44a;
    --text:#4a4a4a;
    --stage:#e6e3df;
  }
  *{box-sizing:border-box;margin:0;padding:0}
  html,body{width:1200px;height:1200px;overflow:hidden;background:var(--stage);font-family:"Open Sans",Arial,sans-serif}
  .spread{position:absolute;left:50px;width:1100px;height:530px;display:flex;box-shadow:0 10px 30px rgba(0,0,0,.25)}
  .spread--outside{top:40px}
  .spread--inside{top:610px}
  .page{position:relative;width:550px;height:530px;overflow:hidden}
  .page--dark{background:var(--ink)}
  .page--light{background:var(--paper)}
  .deco{position:absolute;inset:0;width:100%;height:100%;pointer-events:none}

  .brand{font-weight:600;color:var(--paper);letter-spacing:.5px;display:flex;align-items:center;gap:10px;white-space:nowrap}
  .brand-dot{width:12px;height:12px;border-radius:50%;background:var(--yellow)}

  /* shared website line on both covers */
  .site-line{position:absolute;left:0;right:0;bottom:62px;text-align:center;color:var(--paper);font-weight:700;font-size:16px;line-height:20px;z-index:1}

  /* back cover */
  .contact{position:absolute;left:245px;top:150px;color:var(--paper);font-size:12px}
  .contact-title{color:var(--yellow);font-weight:700;font-size:15px;margin-bottom:10px}
  .contact-row{display:flex;gap:10px;align-items:flex-start;margin-bottom:12px;line-height:1.35}
  .contact-row svg{flex:none;margin-top:1px}
  .back-brand{position:absolute;left:90px;top:340px;font-size:30px}

  /* front cover */
  .front-brand{position:absolute;top:42px;left:0;right:0;justify-content:center;font-size:32px}
  .front-photo{position:absolute;left:0;right:0;top:130px;height:300px;background:radial-gradient(ellipse at 45% 55%,#c8504a 0%,#8a2a22 40%,#4a2414 75%,#2a160c 100%)}

  /* inside left */
  .intro{position:absolute;left:40px;right:40px;top:40px;font-size:12px;line-height:1.6;color:var(--text)}
  .intro p{margin-bottom:14px}
  .steak-photo{position:absolute;left:0;top:230px;width:400px;height:230px;background:radial-gradient(ellipse at 45% 55%,#7a3a22 0%,#4e2214 55%,#e9e4dc 100%)}
  .phone-band{position:absolute;right:0;bottom:0;width:330px;height:52px;background:var(--ink);color:var(--paper);font-weight:700;font-size:17px;display:flex;align-items:center;justify-content:center;clip-path:polygon(10% 0,100% 0,100% 100%,0 100%)}

  /* inside right */
  .products{position:absolute;left:35px;right:30px;top:45px;display:flex;flex-direction:column;gap:26px}
  .product{display:flex;gap:20px;align-items:center}
  .product-photo{flex:none;width:150px;height:105px;border-radius:8px;border:3px solid var(--paper);box-shadow:0 2px 8px rgba(0,0,0,.25)}
  .product-photo--beef{background:radial-gradient(ellipse at center,#c0393a,#7e1f22 70%,#e5d7cc)}
  .product-photo--fish{background:radial-gradient(ellipse at center,#f0a27c,#d9735a 60%,#efe6df)}
  .product-photo--fries{background:radial-gradient(ellipse at center,#f2d36a,#e2b540 55%,#f5f1e6)}
  .product-name{color:var(--red);font-weight:800;font-size:20px;margin-bottom:6px}
  .product-text{font-size:12px;line-height:1.55;color:var(--text)}
  .quality-band{position:absolute;left:0;bottom:0;width:330px;height:46px;background:var(--ink);color:var(--paper);font-weight:700;font-size:14px;display:flex;align-items:center;justify-content:center;clip-path:polygon(0 0,92% 0,100% 100%,0 100%)}
</style>
</head>
<body>

<!-- Outside: back cover + front cover -->
<section class="spread spread--outside">
  <article class="page page--dark back-cover">
    <svg class="deco" viewBox="0 0 550 530" aria-hidden="true">
      <path d="M0 40 Q260 80 550 70 L550 78 Q260 90 0 52 Z" fill="var(--red)"/>
      <path d="M0 58 Q260 96 550 84 L550 90 Q260 104 0 66 Z" fill="var(--yellow)"/>
      <path d="M0 480 L550 470 L550 476 L0 488 Z" fill="var(--yellow)"/>
      <path d="M0 494 L550 482 L550 530 L0 530 Z" fill="var(--red)"/>
      <path d="M0 500 L550 490 L550 530 L0 530 Z" fill="var(--ink-soft)"/>
    </svg>
    <div class="contact">
      <h2 class="contact-title">Fale Conosco</h2>
      <div class="contact-row">
        <svg width="14" height="16" viewBox="0 0 14 16"><path d="M7 0a6 6 0 0 0-6 6c0 4.5 6 10 6 10s6-5.5 6-10a6 6 0 0 0-6-6zm0 8.5A2.5 2.5 0 1 1 7 3.5a2.5 2.5 0 0 1 0 5z" fill="var(--yellow)"/></svg>
        <span>Av. das Acácias, Nº 210<br>Centro / Vila Nova/SP<br>CEP 13480-000</span>
      </div>
      <div class="contact-row">
        <svg width="14" height="14" viewBox="0 0 14 14"><path d="M3 0l2.5 3.5-1.5 1.5c.8 1.8 2.2 3.2 4 4l1.5-1.5L14 10l-1.5 3c-7 0-12.5-5.5-12.5-12.5z" fill="var(--yellow)"/></svg>
        <span>(15) 3421-7760 / (15) 99640-2315</span>
      </div>
      <div class="contact-row">
        <svg width="16" height="12" viewBox="0 0 16 12"><rect width="16" height="12" rx="1.5" fill="var(--yellow)"/><path d="M1 1.5l7 5 7-5" stroke="var(--ink)" stroke-width="1.4" fill="none"/></svg>
        <span>vendas@primeharvest.com.br</span>
      </div>
    </div>
    <div class="brand back-brand"><span>Prime Harvest</span><span class="brand-dot"></span></div>
    <p class="site-line">www.primeharvest.com.br</p>
  </article>

  <article class="page page--dark front-cover">
    <div class="brand front-brand"><span>Prime Harvest</span><span class="brand-dot"></span></div>
    <div class="front-photo" role="img" aria-label="Fotografia de rosbife fatiado sobre tábua de madeira com ramo de alecrim"></div>
    <svg class="deco" viewBox="0 0 550 530" aria-hidden="true">
      <path d="M0 95 Q280 150 550 100 L550 150 Q280 170 0 140 Z" fill="var(--ink)"/>
      <path d="M0 100 Q280 140 550 92 L550 104 Q280 154 0 112 Z" fill="var(--yellow)"/>
      <path d="M0 116 Q280 160 550 110 L550 118 Q280 170 0 126 Z" fill="var(--red)"/>
      <path d="M0 420 L550 405 L550 530 L0 530 Z" fill="var(--ink)"/>
      <path d="M0 418 L550 402 L550 408 L0 424 Z" fill="var(--red)"/>
      <path d="M0 482 L550 470 L550 476 L0 488 Z" fill="var(--yellow)"/>
      <path d="M0 494 L550 482 L550 530 L0 530 Z" fill="var(--red)"/>
      <path d="M0 500 L550 490 L550 530 L0 530 Z" fill="var(--ink-soft)"/>
    </svg>
    <p class="site-line">www.primeharvest.com.br</p>
  </article>
</section>

<!-- Inside: two pages -->
<section class="spread spread--inside">
  <article class="page page--light inside-left">
    <div class="intro">
      <p>Importamos produtos com nossas marcas e distribuímos para supermercados e distribuidores em todo o país.</p>
      <p>Selecionamos cada fornecedor com cuidado para garantir frescor, sabor e qualidade em todas as entregas.</p>
      <p>Logística própria e atendimento dedicado para o seu negócio crescer com segurança.</p>
    </div>
    <div class="steak-photo" role="img" aria-label="Fotografia de bifes grelhados com molho de tomate e salada"></div>
    <svg class="deco" viewBox="0 0 550 530" aria-hidden="true">
      <path d="M0 455 Q160 470 260 530 L0 530 Z" fill="var(--ink)"/>
      <path d="M0 445 Q170 458 280 530 L268 530 Q165 466 0 454 Z" fill="var(--yellow)"/>
      <path d="M0 470 Q140 482 230 530 L218 530 Q135 490 0 478 Z" fill="var(--red)"/>
    </svg>
    <p class="phone-band">(15) 3421-7760</p>
  </article>

  <article class="page page--light inside-right">
    <svg class="deco" viewBox="0 0 550 530" aria-hidden="true">
      <path d="M0 0 L550 0 L550 18 Q280 30 0 14 Z" fill="var(--ink)"/>
      <path d="M0 14 Q280 30 550 18 L550 24 Q280 36 0 20 Z" fill="var(--red)"/>
      <path d="M230 530 Q380 490 550 486 L550 530 Z" fill="var(--ink)"/>
      <path d="M220 530 Q380 482 550 476 L550 484 Q380 490 236 530 Z" fill="var(--yellow)"/>
      <path d="M250 530 Q390 498 550 496 L550 502 Q390 506 266 530 Z" fill="var(--red)"/>
    </svg>
    <div class="products">
      <div class="product">
        <div class="product-photo product-photo--beef" role="img" aria-label="Fotografia de carne bovina fatiada"></div>
        <div>
          <h3 class="product-name">Harvest Beef</h3>
          <p class="product-text">Cortes bovinos selecionados, embalados a vácuo e prontos para a distribuição.</p>
        </div>
      </div>
      <div class="product">
        <div class="product-photo product-photo--fish" role="img" aria-label="Fotografia de filé de salmão"></div>
        <div>
          <h3 class="product-name">Harvest Fish</h3>
          <p class="product-text">Peixes e frutos do mar congelados com padrão de qualidade internacional.</p>
        </div>
      </div>
      <div class="product">
        <div class="product-photo product-photo--fries" role="img" aria-label="Fotografia de batatas fritas palito"></div>
        <div>
          <h3 class="product-name">Harvest Fries</h3>
          <p class="product-text">Batatas pré-fritas crocantes, ideais para restaurantes, lanchonetes e varejo.</p>
        </div>
      </div>
    </div>
    <p class="quality-band">Produtos de qualidade</p>
  </article>
</section>

</body>
</html>
```